Brenvick Holdings LLC, new Business cards

I'm moving offices and need new cards. Plus I'm open to modifying the current design of my card. I will keep the logo but would like to explore other layouts and fonts for the design. I've included the current double sided card for reference. I Like the navy color and white. Might be open to grays or silver. Needs to be clean and elegant.

Target Market(s)

Investors, buyers & sellers of private equities and real estate.

Contact Information for Business Card

Brenvick Holdings
Dorian P.K. Halvers, Managing Principal
418 Ostrander Ave., Suite 612
Denver, CO 80319
M: 970-555-0147, O: 303-555-0192
Dorian@brenvickholdings.example
Brenvickholdings.example

Colors
0354a2
ffffff
c4c4c4

Requirements
Must have
• Business card details.
• Logo raised or embossed, it was designed after a wax seal. Current has raised ink.
Nice to have
• Space on card to write additional notes.

```html
<!DOCTYPE html>
<html lang="en">
<head>
<meta charset="utf-8">
<title>Brenvick Holdings — Business Cards</title>
<link rel="stylesheet" href="https://fonts.googleapis.com/css2?family=Cinzel:wght@400;500&family=Marcellus&family=Open+Sans:wght@400&display=swap">
<style>
  :root {
    --backdrop: #2a2a2c;
    --navy: #24234a;
    --silver: #c4c4c4;
    --silver-light: #e2e2e2;
    --paper: #f1f1f3;
    --ink: #24234a;
  }
  * { box-sizing: border-box; margin: 0; padding: 0; }
  html, body {
    width: 1200px; height: 900px; overflow: hidden;
    background: var(--backdrop);
  }
  .sheet {
    position: relative; width: 1200px; height: 900px;
    display: flex; flex-direction: column; align-items: center; justify-content: center; gap: 30px;
  }
  .card {
    position: relative; width: 700px; height: 400px;
    box-shadow: 0 10px 30px rgba(0,0,0,.45);
  }
  /* Front */
  .card--front { background: var(--navy); color: var(--silver); }
  .seal-mark {
    position: absolute; left: 50%; top: 48px; transform: translateX(-50%);
    display: flex; flex-direction: column; align-items: center; gap: 14px;
  }
  .seal-mark__disc {
    width: 150px; height: 150px; border-radius: 50%;
    background: radial-gradient(circle at 35% 30%, var(--silver-light), var(--silver) 60%, #9d9d9d);
  }
  .seal-mark__name {
    font-family: "Cinzel", serif; font-weight: 500; font-size: 22px; letter-spacing: .14em;
    color: var(--silver); text-transform: uppercase; white-space: nowrap;
  }
  .front-url {
    position: absolute; left: 0; right: 0; top: 278px; text-align: center;
    font-family: "Marcellus", serif; font-size: 17px; letter-spacing: .08em; color: var(--silver);
  }
  .front-tagline {
    position: absolute; left: 0; right: 0; top: 330px; text-align: center;
    font-family: "Marcellus", serif; font-size: 14px; letter-spacing: .12em; color: var(--silver);
    word-spacing: .1em; white-space: nowrap;
  }
  .front-tagline .sep { margin: 0 16px; }

  /* Back */
  .card--back { background: var(--paper); color: var(--ink); }
  .person { position: absolute; left: 56px; top: 52px; }
  .person__name {
    font-family: "Cinzel", serif; font-weight: 400; font-size: 23px; letter-spacing: .05em; text-transform: uppercase;
  }
  .person__title {
    font-family: "Cinzel", serif; font-weight: 400; font-size: 13px; letter-spacing: .06em; text-transform: uppercase; margin-top: 2px;
  }
  .person__rule { width: 48px; height: 2px; background: var(--ink); margin-top: 14px; }
  .contact {
    position: absolute; left: 56px; top: 218px;
    font-family: "Open Sans", sans-serif; font-size: 15px; line-height: 26px;
    display: grid; grid-template-columns: 26px auto; white-space: nowrap;
  }
  .contact dt { font-weight: 400; }
  .contact dd { margin: 0; }
  .back-mark {
    position: absolute; right: 70px; top: 150px;
    display: flex; flex-direction: column; align-items: center; gap: 10px;
  }
  .back-mark__disc { width: 96px; height: 96px; border-radius: 50%; background: var(--ink); }
  .back-mark__name {
    font-family: "Cinzel", serif; font-weight: 500; font-size: 13px; letter-spacing: .12em;
    text-transform: uppercase; color: var(--ink); white-space: nowrap;
  }
</style>
</head>
<body>
<main class="sheet">
  <section class="card card--front" aria-label="Card front">
    <div class="seal-mark">
      <div class="seal-mark__disc" aria-hidden="true"></div>
      <div class="seal-mark__name">Brenvick Holdings</div>
    </div>
    <p class="front-url">BRENVICKHOLDINGS.EXAMPLE</p>
    <p class="front-tagline">FAMILY OFFICE INVESTMENT FIRM<span class="sep">I</span>PRIVATE EQUITY<span class="sep">I</span>REAL ESTATE</p>
  </section>

  <section class="card card--back" aria-label="Card back">
    <div class="person">
      <h1 class="person__name">Dorian P.K. Halvers</h1>
      <p class="person__title">Managing Principal</p>
      <div class="person__rule"></div>
    </div>
    <dl class="contact">
      <dt>A:</dt><dd>418 Ostrander Ave., Suite 612</dd>
      <dt></dt><dd>Denver, CO 80319</dd>
      <dt>P:</dt><dd>970-555-0147, O: 303-555-0192</dd>
      <dt>E:</dt><dd>Dorian@brenvickholdings.example</dd>
    </dl>
    <div class="back-mark">
      <div class="back-mark__disc" aria-hidden="true"></div>
      <div class="back-mark__name">Brenvick Holdings</div>
    </div>
  </section>
</main>
</body>
</html>
```